Modern Business Card for Speech Therapy Practice
Clear Sound Harbor LLC
Bright & Fun-filled
Odile Varnet, M.A., CCC-SLP
827 Quarry Ln.
Fernhollow, ST 07391
Odile.Varnet@mailbrook.net
www.ClearSoundHarbor.net
NJ Lic: 58KT00394817

```html
<!DOCTYPE html>
<html lang="en">
<head>
<meta charset="utf-8">
<title>Clear Sound Harbor LLC – Stationery</title>
<link rel="stylesheet" href="https://fonts.googleapis.com/css2?family=Arimo:wght@400;700&family=Open+Sans:wght@400;600&display=swap">
<style>
  :root {
    --navy: #2c3a8e;
    --ink: #1d1d1f;
    --grey: #6d6f73;
    --paper: #ffffff;
    --backdrop: #ecedef;
    --orange: #ef8a25;
    --line: #222222;
  }
  * { box-sizing: border-box; margin: 0; padding: 0; }
  html, body { width: 1200px; height: 936px; overflow: hidden; }
  body {
    background: var(--backdrop);
    font-family: "Open Sans", Arial, sans-serif;
    color: var(--ink);
    position: relative;
  }
  .sheet { position: absolute; background: var(--paper); overflow: hidden; }

  .brand {
    display: flex; align-items: center; gap: 6px;
    font-family: "Arimo", Arial, sans-serif; font-weight: 700;
    color: var(--ink); white-space: nowrap; letter-spacing: -0.3px;
  }
  .brand .dot { border-radius: 50%; background: var(--orange); flex: none; }

  .url {
    position: absolute; color: #fff; font-size: 9px; letter-spacing: 2px;
    font-family: "Open Sans", Arial, sans-serif; white-space: nowrap;
  }
  .band { position: absolute; left: 0; width: 100%; }

  /* Letterhead */
  .letterhead { left: 185px; top: 63px; width: 386px; height: 552px; }
  .letterhead .brand { position: absolute; left: 26px; top: 44px; font-size: 17px; }
  .letterhead .brand .dot { width: 12px; height: 12px; }
  .letterhead .contact {
    position: absolute; left: 268px; top: 20px; font-size: 6.5px; line-height: 12px; color: var(--grey);
  }
  .letterhead .contact li { list-style: none; display: flex; align-items: center; gap: 4px; white-space: nowrap; }
  .letterhead .contact li::before {
    content: ""; width: 5px; height: 5px; border-radius: 50%; background: var(--navy); flex: none;
  }
  .letterhead .faint-mark {
    position: absolute; left: 143px; top: 210px; width: 100px; height: 100px;
    border-radius: 50%; background: #f3f3f4;
  }
  .letterhead .band { bottom: 0; height: 50px; }
  .letterhead .url { right: 14px; bottom: 20px; font-size: 7px; }

  /* Presentation folder */
  .folder { left: 635px; top: 46px; width: 495px; height: 571px; }
  .folder .brand { position: absolute; left: 50%; top: 240px; transform: translateX(-50%); font-size: 40px; gap: 12px; }
  .folder .brand .dot { width: 30px; height: 30px; }
  .folder .band { bottom: 0; height: 60px; }
  .folder .url { right: 24px; bottom: 20px; }

  /* Business cards */
  .card-front { left: 43px; top: 673px; width: 198px; height: 102px; }
  .card-front .brand { position: absolute; left: 10px; top: 20px; font-size: 10px; gap: 3px; }
  .card-front .brand .dot { width: 7px; height: 7px; }
  .card-front .person {
    position: absolute; right: 10px; top: 14px; text-align: right; font-size: 5px; line-height: 7.5px; color: var(--grey);
  }
  .card-front .person strong { display: block; font-size: 6.5px; color: var(--ink); font-weight: 600; }
  .card-front .band { bottom: 0; height: 22px; background: var(--navy); }
  .card-front .band::before { content: ""; position: absolute; left: 0; top: -3px; width: 100%; height: 2px; background: var(--line); }

  .card-back { left: 43px; top: 792px; width: 198px; height: 107px; }
  .card-back .brand { position: absolute; left: 50%; top: 38px; transform: translateX(-50%); font-size: 10px; gap: 3px; }
  .card-back .brand .dot { width: 7px; height: 7px; }
  .card-back .license {
    position: absolute; left: 0; width: 100%; bottom: 14px; text-align: center; font-size: 5px; color: var(--grey); letter-spacing: .5px;
  }

  /* Envelope front */
  .envelope-front { left: 267px; top: 668px; width: 432px; height: 231px; }
  .envelope-front .brand { position: absolute; left: 22px; top: 40px; font-size: 14px; gap: 5px; }
  .envelope-front .brand .dot { width: 10px; height: 10px; }
  .envelope-front .return {
    position: absolute; left: 22px; top: 76px; font-size: 7px; letter-spacing: 1.6px; color: var(--ink);
  }

  /* Envelope back */
  .envelope-back { left: 742px; top: 668px; width: 421px; height: 231px; }
  .envelope-back .flap { position: absolute; left: 0; top: 0; width: 100%; height: 56px; }
  .envelope-back .url { left: 0; width: 100%; text-align: center; top: 12px; }
</style>
</head>
<body>

  <section class="sheet letterhead" aria-label="Letterhead">
    <div class="brand"><span class="dot"></span>Clear Sound Harbor</div>
    <ul class="contact">
      <li>827 Quarry Ln.<br>Fernhollow, ST 07391</li>
      <li>Tel (201) 555-0148</li>
      <li>Odile.Varnet@mailbrook.net</li>
      <li>www.ClearSoundHarbor.net</li>
    </ul>
    <div class="faint-mark" aria-hidden="true"></div>
    <svg class="band" viewBox="0 0 386 50" preserveAspectRatio="none" aria-hidden="true">
      <path d="M0 24 H180 L196 10 H386 V14 H198 L182 28 H0 Z" fill="var(--line)"/>
      <path d="M0 32 H184 L200 18 H386 V50 H0 Z" fill="var(--navy)"/>
    </svg>
    <span class="url">www.ClearSoundHarbor.net</span>
  </section>

  <section class="sheet folder" aria-label="Presentation folder">
    <div class="brand"><span class="dot"></span>Clear Sound Harbor</div>
    <svg class="band" viewBox="0 0 495 60" preserveAspectRatio="none" aria-hidden="true">
      <path d="M0 24 H210 Q232 24 244 10 Q252 2 270 2 H495 V7 H272 Q256 7 249 15 Q236 29 212 29 H0 Z" fill="var(--line)"/>
      <path d="M0 34 H214 Q238 34 252 18 Q260 10 274 10 H495 V60 H0 Z" fill="var(--navy)"/>
    </svg>
    <span class="url">www.ClearSoundHarbor.net</span>
  </section>

  <section class="sheet card-front" aria-label="Business card front">
    <div class="brand"><span class="dot"></span>Clear Sound Harbor</div>
    <div class="person">
      <strong>Odile Varnet</strong>
      M.A., CCC-SLP<br>
      Tel (201) 555-0148<br>
      Odile.Varnet@mailbrook.net
    </div>
    <div class="band"></div>
  </section>

  <section class="sheet card-back" aria-label="Business card back">
    <div class="brand"><span class="dot"></span>Clear Sound Harbor</div>
    <p class="license">NJ Lic: 58KT00394817 · www.ClearSoundHarbor.net</p>
  </section>

  <section class="sheet envelope-front" aria-label="Envelope front">
    <div class="brand"><span class="dot"></span>Clear Sound Harbor</div>
    <p class="return">827 Quarry Ln. Fernhollow, ST 07391</p>
  </section>

  <section class="sheet envelope-back" aria-label="Envelope back">
    <svg class="flap" viewBox="0 0 421 56" preserveAspectRatio="none" aria-hidden="true">
      <path d="M0 0 H421 V34 H0 Z" fill="var(--navy)"/>
      <path d="M0 38 H421 V41 H0 Z" fill="var(--line)"/>
    </svg>
    <span class="url">www.ClearSoundHarbor.net</span>
  </section>

</body>
</html>
```